Design a web site for my business - Brellan Coatworks Mackaby.

We are a family business that handles design, fabrication and installation of powder coated aluminum, stainless steel and glass products. Including handrails, privacy slat screens, electric gates and pool fencing. We are based in the Whitsundays in North Queensland and service an area from Airlie Beach to Townsville.

Target Market(s)

Domestic and commercial

Industry/Entity Type

fabrication - manufacturing

Coding

Coded - Design and coding required

Number of Pages Required

5+ page

Colors
0054AA
0677BA
7BADD7
CADEEF
E8F1F8

Requirements
Must have
• photo galleries, contact page, one page for privacy screens, balustrades, glass fencing, stainless steel handrail, powder coated aluminium handrails and pool fencing

```html
<!DOCTYPE html>
<html lang="en">
<head>
<meta charset="utf-8">
<title>Brellan Coatworks Mackaby</title>
<link href="https://fonts.googleapis.com/css2?family=Manrope:wght@400;500;600;700;800&family=Newsreader:opsz,wght@6..72,400&display=swap" rel="stylesheet">
<style>
:root{
  --ink:#0b1622;
  --panel:#0f1e2d;
  --cta:#0a2c52;
  --paper:#e8f1f8;
  --paper-2:#f1f6fb;
  --white:#ffffff;
  --muted:#cadeef;
  --text:#22303c;
  --blue:#0054aa;
  --blue-2:#0677ba;
  --sky:#7badd7;
  --line:#2f4a63;
  --sans:'Manrope',Arial,sans-serif;
  --serif:'Newsreader',Georgia,serif;
}
*{box-sizing:border-box;margin:0;padding:0}
html,body{width:1200px;height:2529px;overflow:hidden}
body{position:relative;background:var(--ink);font-family:var(--sans);color:var(--text)}
.abs{position:absolute}
.photo{position:absolute}
.btn{position:absolute;display:flex;align-items:center;justify-content:center;gap:12px;font-size:11px;font-weight:700;letter-spacing:.08em;text-transform:uppercase;white-space:nowrap}
.btn svg{width:13px;height:13px}
.eyebrow{font-size:9.5px;font-weight:700;letter-spacing:.1em;text-transform:uppercase}
.serif-h{font-family:var(--serif);font-weight:400;font-size:29px;line-height:35px;color:var(--ink)}

/* hero */
.hero{position:absolute;left:0;top:0;width:1200px;height:667px;overflow:hidden}
.hero .photo{inset:0;background:linear-gradient(180deg,#2e3b48 0%,#4d5d6a 22%,#2c3a2a 34%,#42505c 48%,#55708a 65%,#2c3944 100%)}
.hero .shade{position:absolute;inset:0;background:linear-gradient(90deg,#08111a 0%,rgba(8,17,26,.92) 30%,rgba(8,17,26,.45) 48%,rgba(8,17,26,0) 65%)}
.logo{position:absolute;left:74px;top:150px;display:flex;align-items:center;gap:10px;color:var(--white)}
.logo .mark{width:16px;height:16px;border:2px solid var(--white)}
.logo .name{font-size:20px;font-weight:700;line-height:24px}
.nav{position:absolute;top:48px;left:466px;display:flex;gap:33px;font-size:10.5px;font-weight:600;letter-spacing:.06em;color:var(--white)}
.quote-btn{left:1031px;top:37px;width:132px;height:37px;border:1px solid var(--white);color:var(--white);font-size:10px}
.hero .tag{left:74px;top:247px;color:var(--white);font-size:15px;letter-spacing:.2em;font-weight:500}
.hero h1{position:absolute;left:72px;top:278px;color:var(--white);font-size:53px;line-height:61px;font-weight:700;letter-spacing:-.01em}
.hero p{position:absolute;left:74px;top:415px;width:300px;color:#e4ecf2;font-size:14.5px;line-height:25.5px}
.btn-primary{left:74px;top:541px;width:160px;height:42px;background:var(--blue);color:var(--white)}
.btn-ghost{left:255px;top:541px;width:186px;height:42px;border:1px solid var(--white);color:var(--white)}

/* features */
.features{position:absolute;left:0;top:667px;width:1200px;height:179px;background:var(--panel)}
.feature{position:absolute;top:30px;color:var(--white)}
.feature svg{width:34px;height:34px;stroke:var(--sky);fill:none;stroke-width:1.4}
.feature h3{margin-top:10px;font-size:12px;font-weight:700}
.feature p{margin-top:5px;font-size:11px;line-height:20px;color:var(--muted)}
.divider{position:absolute;top:36px;width:1px;height:100px;background:var(--line)}

/* products */
.products{position:absolute;left:0;top:846px;width:1200px;height:367px;background:var(--paper)}
.products .eyebrow{position:absolute;left:74px;top:57px;color:var(--blue);font-size:9px}
.products .serif-h{position:absolute;left:73px;top:79px}
.products p{position:absolute;left:74px;top:166px;width:225px;font-size:11px;line-height:20px}
.btn-outline{border:1px solid var(--blue);color:var(--ink);font-size:9.5px}
.products .btn-outline{left:74px;top:268px;width:162px;height:34px}
.tile{position:absolute;top:57px;height:246px}
.tile-label{position:absolute;top:316px;display:flex;gap:9px;align-items:center;font-size:10px;font-weight:700;letter-spacing:.06em;color:var(--ink)}
.tile-label svg{width:11px;height:11px;color:var(--blue)}

/* built for */
.built{position:absolute;left:0;top:1213px;width:1200px;height:368px}
.built .left{position:absolute;left:0;top:0;width:442px;height:368px;background:var(--panel);color:var(--white)}
.built .photo{left:442px;top:0;width:758px;height:368px;background:linear-gradient(160deg,#55606a 0%,#3a3329 30%,#2b3531 55%,#3e5a3a 78%,#1f2c22 100%)}
.built .eyebrow{position:absolute;left:74px;top:47px;font-size:9px;color:var(--sky)}
.built .serif-h{position:absolute;left:73px;top:66px;color:var(--white);line-height:37px}
.built p{position:absolute;left:74px;top:152px;width:280px;font-size:11px;line-height:20px;color:var(--muted)}
.stat{position:absolute;top:238px}
.stat b{display:block;font-family:var(--serif);font-weight:400;font-size:25px}
.stat span{display:block;margin-top:8px;font-size:7.5px;line-height:11px;letter-spacing:.04em;color:var(--muted);text-transform:uppercase}
.stat-line{position:absolute;top:241px;width:1px;height:56px;background:var(--line)}

/* process */
.process{position:absolute;left:0;top:1581px;width:1200px;height:287px;background:var(--paper-2)}
.process .eyebrow{position:absolute;left:74px;top:46px;color:var(--blue);font-size:9px}
.process .serif-h{position:absolute;left:73px;top:65px}
.process p.lead{position:absolute;left:74px;top:146px;width:190px;font-size:11px;line-height:20px}
.process .btn-outline{left:74px;top:205px;width:140px;height:35px}
.step{position:absolute;top:67px;width:125px}
.step svg.icon{width:36px;height:36px;stroke:var(--blue);fill:none;stroke-width:1.4}
.step .num{margin-top:13px;font-size:12px;color:var(--ink);font-weight:600}
.step h3{margin-top:10px;font-size:12px;letter-spacing:.05em;font-weight:700;color:var(--ink)}
.step p{margin-top:6px;font-size:11px;line-height:20px}
.arrow{position:absolute;top:112px;width:44px;height:12px;stroke:var(--blue-2);fill:none;stroke-width:1.3}

/* projects */
.projects{position:absolute;left:0;top:1868px;width:1200px;height:286px;background:var(--paper)}
.projects .eyebrow{position:absolute;left:74px;top:40px;color:var(--blue);font-size:9px}
.projects .serif-h{position:absolute;left:73px;top:59px}
.projects p{position:absolute;left:74px;top:140px;width:200px;font-size:11px;line-height:20px}
.projects .btn-outline{left:74px;top:218px;width:160px;height:34px}

/* cta */
.cta{position:absolute;left:0;top:2154px;width:1200px;height:124px;background:var(--cta);color:var(--white)}
.cta .bubble{position:absolute;left:85px;top:33px;width:62px;height:62px;border:1.5px solid var(--sky);border-radius:50%}
.cta .bubble svg{position:absolute;left:17px;top:17px;width:28px;height:28px;stroke:var(--paper);fill:none;stroke-width:1.5}
.cta .vline{position:absolute;left:170px;top:28px;width:1px;height:70px;background:#2e5b8a}
.cta .eyebrow{position:absolute;left:193px;top:25px;font-size:8px;color:var(--muted)}
.cta h2{position:absolute;left:193px;top:44px;font-family:var(--serif);font-weight:400;font-size:26px;line-height:32px}
.cta .btn{left:919px;top:47px;width:145px;height:36px;border:1px solid var(--white);font-size:9.5px}

/* footer */
.footer{position:absolute;left:0;top:2278px;width:1200px;height:251px;background:var(--ink);color:#dfe8ef}
.footer .logo{left:74px;top:36px}
.footer .logo .name{font-size:16px;line-height:20px}
.footer .about{position:absolute;left:74px;top:85px;width:215px;font-size:10.5px;line-height:20.5px;color:#c3d3e0}
.social{position:absolute;left:74px;top:184px;display:flex;gap:20px}
.social span{width:12px;height:12px;border:1.4px solid #cadeef;border-radius:3px}
.social span.round{border-radius:50%}
.fcol{position:absolute;top:45px}
.fcol h4{font-size:9px;letter-spacing:.1em;font-weight:700;margin-bottom:14px;color:var(--white)}
.fcol li{list-style:none;font-size:10.5px;line-height:26px;color:#c3d3e0}
.contact li{display:flex;align-items:center;gap:9px}
.contact svg{width:12px;height:12px;stroke:var(--sky);fill:none;stroke-width:1.5}
.footer .btn{left:908px;top:154px;width:125px;height:34px;border:1px solid var(--white);color:var(--white);font-size:9.5px}
.copy{position:absolute;left:74px;top:226px;font-size:8.5px;color:#8fa3b4}
.legal{position:absolute;left:908px;top:226px;display:flex;gap:16px;font-size:8.5px;color:#8fa3b4}
</style>
</head>
<body>

<header class="hero">
  <div class="photo" role="img" aria-label="Timber-capped powder coated handrail along a rocky waterfront boardwalk with palms and homes"></div>
  <div class="shade"></div>
  <div class="logo"><span class="mark"></span><span class="name">Brellan Coatworks<br>Mackaby</span></div>
  <nav class="nav"><span>HOME</span><span>ABOUT</span><span>SERVICES</span><span>PRODUCTS</span><span>PROJECTS</span><span>GALLERY</span><span>CONTACT</span></nav>
  <a class="btn quote-btn">Get a quote <svg viewBox="0 0 14 14" fill="none" stroke="currentColor" stroke-width="1.4"><path d="M2 7h10M8 3l4 4-4 4"/></svg></a>
  <div class="abs tag">DESIGN. FABRICATE. INSTALL.</div>
  <h1>Quality Crafted.<br>Built to Last.</h1>
  <p>Specialists in powder coated aluminium, stainless steel and glass solutions for residential and commercial spaces across the Whitsundays.</p>
  <a class="btn btn-primary">Our products <svg viewBox="0 0 14 14" fill="none" stroke="currentColor" stroke-width="1.4"><path d="M2 7h10M8 3l4 4-4 4"/></svg></a>
  <a class="btn btn-ghost">View our work <svg viewBox="0 0 14 14" fill="none" stroke="currentColor" stroke-width="1.4"><path d="M2 7h10M8 3l4 4-4 4"/></svg></a>
</header>

<section class="features">
  <div class="feature" style="left:107px"><svg viewBox="0 0 34 34"><path d="M5 27L25 7l3 3L8 30z M4 6l6-2 22 22-2 6-6-2z"/></svg><h3>Custom Designed</h3><p>Tailored solutions to<br>suit your space.</p></div>
  <div class="divider" style="left:309px"></div>
  <div class="feature" style="left:367px"><svg viewBox="0 0 34 34"><path d="M17 3l12 4v10c0 7-5 12-12 14C10 29 5 24 5 17V7z M17 7l8 3v7c0 5-3 8-8 10"/></svg><h3>Premium Materials</h3><p>Aluminium, stainless steel<br>and glass built to perform.</p></div>
  <div class="divider" style="left:557px"></div>
  <div class="feature" style="left:617px"><svg viewBox="0 0 34 34"><circle cx="17" cy="17" r="5"/><path d="M17 3v5M17 26v5M3 17h5M26 17h5M7 7l3.5 3.5M23.5 23.5L27 27M7 27l3.5-3.5M23.5 10.5L27 7"/><circle cx="17" cy="17" r="10"/></svg><h3>Quality Powder Coating</h3><p>Durable finishes. Superior<br>protection. Built for our climate.</p></div>
  <div class="divider" style="left:834px"></div>
  <div class="feature" style="left:891px"><svg viewBox="0 0 34 34"><circle cx="17" cy="17" r="15"/><path d="M10 17l5 5 9-10"/></svg><h3>End to End Service</h3><p>Design, fabrication and installation<br>– handled with care.</p></div>
</section>

<section class="products">
  <div class="eyebrow">Our products</div>
  <h2 class="serif-h">Functional. Beautiful.<br>Built for outdoor living.</h2>
  <p>From sleek pool fencing to custom gates and handrails, we deliver premium solutions that combine safety, style and strength.</p>
  <a class="btn btn-outline">Explore products <svg viewBox="0 0 14 14" fill="none" stroke="currentColor" stroke-width="1.4"><path d="M2 7h10M8 3l4 4-4 4"/></svg></a>
  <div class="tile photo" style="left:371px;width:179px;background:linear-gradient(180deg,#5a6a78,#3b3f35 45%,#7a4a2a 75%,#5c5e5e)" role="img" aria-label="Timber-topped black handrail beside waterfront rocks"></div>
  <div class="tile photo" style="left:564px;width:182px;background:linear-gradient(180deg,#4f6a58,#2a2522 30%,#3a322c 80%,#51554a)" role="img" aria-label="Dark horizontal slat privacy screen"></div>
  <div class="tile photo" style="left:760px;width:184px;background:linear-gradient(180deg,#8c9aa6,#cfcac0 40%,#b9b3a7 75%,#7f7e78)" role="img" aria-label="Cream slatted electric gate in front of a house"></div>
  <div class="tile photo" style="left:958px;width:184px;background:linear-gradient(180deg,#5f8a5c,#6fa09a 45%,#4f9a97 70%,#5d5f5c)" role="img" aria-label="Frameless glass pool fence beside clear water"></div>
  <div class="tile-label" style="left:372px">HANDRAILS <svg viewBox="0 0 14 14" fill="none" stroke="currentColor" stroke-width="1.5"><path d="M2 7h10M8 3l4 4-4 4"/></svg></div>
  <div class="tile-label" style="left:565px">PRIVACY SCREENS <svg viewBox="0 0 14 14" fill="none" stroke="currentColor" stroke-width="1.5"><path d="M2 7h10M8 3l4 4-4 4"/></svg></div>
  <div class="tile-label" style="left:761px">ELECTRIC GATES <svg viewBox="0 0 14 14" fill="none" stroke="currentColor" stroke-width="1.5"><path d="M2 7h10M8 3l4 4-4 4"/></svg></div>
  <div class="tile-label" style="left:959px">POOL FENCING <svg viewBox="0 0 14 14" fill="none" stroke="currentColor" stroke-width="1.5"><path d="M2 7h10M8 3l4 4-4 4"/></svg></div>
</section>

<section class="built">
  <div class="left">
    <div class="eyebrow">Built for</div>
    <h2 class="serif-h">Functional Conditions.<br>Everyday Living.</h2>
    <p>We use premium materials and industry leading powder coating to ensure long-lasting performance in the harshest environments.</p>
    <div class="stat" style="left:74px"><b>10+</b><span>Years experience</span></div>
    <div class="stat-line" style="left:162px"></div>
    <div class="stat" style="left:185px"><b>100%</b><span>Australian made<br>&amp; owned</span></div>
    <div class="stat-line" style="left:286px"></div>
    <div class="stat" style="left:309px"><b>5★</b><span>Quality &amp; service<br>you can trust</span></div>
  </div>
  <div class="photo" role="img" aria-label="Elevated timber house with stainless balustrade and glass fencing among tropical plants"></div>
</section>

<section class="process">
  <div class="eyebrow">Our process</div>
  <h2 class="serif-h">Simple. Seamless.<br>Stress-Free.</h2>
  <p class="lead">We make the process easy from concept to completion.</p>
  <a class="btn btn-outline">How we work <svg viewBox="0 0 14 14" fill="none" stroke="currentColor" stroke-width="1.4"><path d="M2 7h10M8 3l4 4-4 4"/></svg></a>

  <div class="step" style="left:372px"><svg class="icon" viewBox="0 0 36 36"><circle cx="18" cy="13" r="9"/><circle cx="18" cy="13" r="4"/><path d="M14 22v6h8v-6M15 31h6"/></svg><div class="num">01</div><h3>CONSULT</h3><p>We listen, understand and offer expert advice.</p></div>
  <svg class="arrow" style="left:477px" viewBox="0 0 44 12"><path d="M0 6h42M36 1l6 5-6 5"/></svg>
  <div class="step" style="left:566px"><svg class="icon" viewBox="0 0 36 36"><path d="M6 30l3-9L26 4l6 6-17 17z M23 7l6 6"/></svg><div class="num">02</div><h3>DESIGN</h3><p>Custom designs tailored to your space and needs.</p></div>
  <svg class="arrow" style="left:670px" viewBox="0 0 44 12"><path d="M0 6h42M36 1l6 5-6 5"/></svg>
  <div class="step" style="left:761px"><svg class="icon" viewBox="0 0 36 36"><circle cx="18" cy="18" r="5"/><circle cx="18" cy="18" r="11"/><path d="M18 3v4M18 29v4M3 18h4M29 18h4M7.5 7.5l3 3M25.5 25.5l3 3M7.5 28.5l3-3M25.5 10.5l3-3"/></svg><div class="num">03</div><h3>FABRICATE</h3><p>Precision made in-house using premium materials and finishes.</p></div>
  <svg class="arrow" style="left:867px" viewBox="0 0 44 12"><path d="M0 6h42M36 1l6 5-6 5"/></svg>
  <div class="step" style="left:959px"><svg class="icon" viewBox="0 0 36 36"><path d="M5 9l8-3 10 3 8-3v20l-8 3-10-3-8 3z M13 6v20M23 9v20"/></svg><div class="num">04</div><h3>INSTALL</h3><p>Professional installation with attention to detail every time.</p></div>
</section>

<section class="projects">
  <div class="eyebrow">Recent projects</div>
  <h2 class="serif-h">Built with pride.<br>Installed with care.</h2>
  <p>See how we bring ideas to life with quality craftsmanship and lasting results.</p>
  <a class="btn btn-outline">View all projects <svg viewBox="0 0 14 14" fill="none" stroke="currentColor" stroke-width="1.4"><path d="M2 7h10M8 3l4 4-4 4"/></svg></a>
  <div class="photo" style="left:371px;top:0;width:261px;height:286px;background:linear-gradient(170deg,#6c7c6a,#3b4e2f 35%,#5a4634 70%,#7a7064)" role="img" aria-label="Timber boardwalk with stainless handrail through tropical garden"></div>
  <div class="photo" style="left:636px;top:0;width:282px;height:286px;background:linear-gradient(180deg,#4e6b3a,#6e8e66 45%,#9a8f7e 75%,#b8b2a8)" role="img" aria-label="Glass fencing above stone steps in a garden"></div>
  <div class="photo" style="left:923px;top:0;width:277px;height:286px;background:linear-gradient(170deg,#7f8890,#4a3a2c 35%,#6e7b80 65%,#3d4a36)" role="img" aria-label="Glass balustrade beneath an elevated timber home"></div>
</section>

<section class="cta">
  <div class="bubble"><svg viewBox="0 0 28 28"><path d="M14 4C8 4 3 8 3 13c0 3 1.5 5 4 7l-1 5 5-3c1 .3 2 .4 3 .4 6 0 11-4 11-9.4S20 4 14 4z"/><path d="M9 13h.5M14 13h.5M19 13h.5"/></svg></div>
  <div class="vline"></div>
  <div class="eyebrow">Ready to get started?</div>
  <h2>Let’s build something<br>exceptional together.</h2>
  <a class="btn">Get in touch <svg viewBox="0 0 14 14" fill="none" stroke="currentColor" stroke-width="1.4"><path d="M2 7h10M8 3l4 4-4 4"/></svg></a>
</section>

<footer class="footer">
  <div class="logo"><span class="mark"></span><span class="name">Brellan Coatworks<br>Mackaby</span></div>
  <p class="about">Specialists in powder coated aluminium, stainless steel and glass products. Proudly servicing the Whitsundays and surrounding areas.</p>
  <div class="social"><span></span><span class="round"></span><span></span></div>
  <div class="fcol" style="left:391px"><h4>PRODUCTS</h4><ul><li>Handrails</li><li>Privacy Screens</li><li>Electric Gates</li><li>Pool Fencing</li></ul></div>
  <div class="fcol" style="left:565px"><h4>SERVICES</h4><ul><li>Design</li><li>Fabrication</li><li>Installation</li><li>Powder Coating</li></ul></div>
  <div class="fcol" style="left:746px"><h4>COMPANY</h4><ul><li>About Us</li><li>Our Process</li><li>Projects</li><li>Gallery</li></ul></div>
  <div class="fcol contact" style="left:908px"><h4>CONTACT</h4><ul>
    <li><svg viewBox="0 0 12 12"><path d="M2 1h2l1 3-1.5 1a6 6 0 003 3L8 7l3 1v2c0 .6-.4 1-1 1A9 9 0 011 2c0-.6.4-1 1-1z"/></svg>0400 555 018</li>
    <li><svg viewBox="0 0 12 12"><rect x="1" y="2.5" width="10" height="7"/><path d="M1 3l5 4 5-4"/></svg>hello@brellancoatworks.example</li>
    <li><svg viewBox="0 0 12 12"><path d="M6 11s4-4 4-6.5a4 4 0 00-8 0C2 7 6 11 6 11z"/><circle cx="6" cy="4.5" r="1.3"/></svg>Whitsundays, QLD</li>
  </ul></div>
  <a class="btn">Get a quote <svg viewBox="0 0 14 14" fill="none" stroke="currentColor" stroke-width="1.4"><path d="M2 7h10M8 3l4 4-4 4"/></svg></a>
  <div class="copy">© 2024 Brellan Coatworks Mackaby. All rights reserved.</div>
  <div class="legal"><span>Privacy Policy</span><span>Terms &amp; Conditions</span></div>
</footer>

</body>
</html>
```